Criação de Papelaria Profissional para Advocacia e Direito
A empresa queria:
" Ribeiro Tavares Advogados é um escritório boutique de atuação diversificada (full service) "

```html
<!DOCTYPE html>
<html lang="pt-BR">
<head>
<meta charset="utf-8">
<title>Ribeiro Tavares Advogados — Envelope</title>
<link href="https://fonts.googleapis.com/css2?family=Montserrat:wght@400;500;600;700&display=swap" rel="stylesheet">
<style>
  :root {
    --navy: #344e63;
    --navy-deep: #2c4456;
    --grey-text: #9aa3aa;
    --paper: #ffffff;
    --paper-shade: #e9eaeb;
    --backdrop: #ececec;
    --contact: #e6ebef;
  }
  * { margin: 0; padding: 0; box-sizing: border-box; }
  html, body { width: 1200px; height: 1200px; overflow: hidden; }
  body {
    background: var(--backdrop);
    font-family: "Montserrat", Arial, sans-serif;
    position: relative;
  }
  .envelope {
    position: absolute;
    top: 305px;
    width: 511px;
    height: 614px;
    box-shadow: 0 6px 18px rgba(0,0,0,0.18);
  }
  .envelope-back {
    left: 67px;
    background: var(--navy);
  }
  .back-mark {
    position: absolute;
    left: 161px;
    top: 408px;
    width: 188px;
    height: 80px;
    border: 3px solid rgba(255,255,255,0.08);
  }
  .back-contact {
    position: absolute;
    left: 204px;
    top: 516px;
    color: var(--contact);
    font-size: 10px;
    line-height: 19px;
    letter-spacing: 0.2px;
  }
  .back-contact .cities { font-weight: 700; }
  .envelope-front {
    left: 624px;
    background: linear-gradient(180deg, var(--paper) 0%, var(--paper) 55%, var(--paper-shade) 100%);
    overflow: hidden;
  }
  .flap {
    position: absolute;
    left: 0; top: 0;
    width: 511px;
    height: 70px;
    display: block;
  }
  .brand {
    position: absolute;
    left: 0; right: 0;
    top: 256px;
    text-align: center;
  }
  .brand-square {
    display: block;
    margin: 0 auto 6px;
    width: 40px;
    height: 22px;
    border: 2px solid var(--navy);
  }
  .brand-name {
    display: block;
    color: var(--navy);
    font-weight: 500;
    font-size: 33px;
    letter-spacing: 2px;
    line-height: 1;
  }
  .brand-tagline {
    display: block;
    margin-top: 5px;
    color: var(--grey-text);
    font-weight: 600;
    font-size: 8px;
    letter-spacing: 2.4px;
  }
</style>
</head>
<body>
  <section class="envelope envelope-back">
    <div class="back-mark" aria-hidden="true"></div>
    <div class="back-contact">
      <p class="cities">SÃO PAULO | BRASÍLIA</p>
      <p>www.ribeirotavares.com.br</p>
      <p>+55 11 3040 7182 | SP</p>
      <p>+55 61 3251 6490 | DF</p>
    </div>
  </section>

  <section class="envelope envelope-front">
    <svg class="flap" viewBox="0 0 511 70" aria-hidden="true">
      <defs>
        <linearGradient id="flapShadow" x1="0" y1="0" x2="0" y2="1">
          <stop offset="0" stop-color="#000" stop-opacity="0.22"/>
          <stop offset="1" stop-color="#000" stop-opacity="0"/>
        </linearGradient>
      </defs>
      <path d="M0 44 L24 62 L487 62 L511 44 Z" fill="url(#flapShadow)"/>
      <path d="M0 0 L511 0 L511 42 L482 56 L29 56 L0 42 Z" fill="var(--navy-deep)"/>
    </svg>
    <div class="brand">
      <span class="brand-square" aria-hidden="true"></span>
      <span class="brand-name">RIBEIRO TAVARES</span>
      <span class="brand-tagline">ADVOGADOS &amp; CONSULTORES</span>
    </div>
  </section>
</body>
</html>
```